Refresh Application User Interface

Brindlecove wishes to update the look of its business applications. Two representative forms are shown below. Please note, we are not considering changes in functionality or usability. Our goal is a cleaner, more contemporary design.

Industry/Entity Type

Business

```html
<!DOCTYPE html>
<html lang="en">
<head>
<meta charset="utf-8">
<title>Brindlecove – Purchase Order</title>
<link href="https://fonts.googleapis.com/css2?family=Roboto:wght@400;500;700&display=swap" rel="stylesheet">
<style>
:root{
  --blue:#0b51a1;
  --green:#9ccf63;
  --green-dark:#7fb046;
  --text:#333;
  --field:#c9c9c9;
  --white:#fff;
}
*{box-sizing:border-box;margin:0;padding:0}
html,body{width:1200px;height:1170px;overflow:hidden;background:var(--white);font-family:Roboto,sans-serif;color:var(--text)}
.abs{position:absolute}
.flex{display:flex;align-items:center;justify-content:center}
.topbar{left:0;top:0;width:1200px;height:50px;background:var(--blue);color:var(--white);font-size:18px}
.topbar .cell{position:absolute;top:0;height:50px;display:flex;align-items:center;gap:8px}
.topbar .hl{background:var(--green);font-weight:700;padding:0 10px}
.toplinks{right:130px;top:0;height:50px;display:flex;align-items:center;font-size:14px}
.toplinks span{padding:0 9px;border-left:1px solid var(--white);line-height:18px}
.toplinks span:first-child{border-left:none}
.logo{left:1032px;top:64px;font-size:24px;font-weight:700;color:var(--blue);letter-spacing:.5px}
.apptab{top:65px;height:33px;background:var(--blue);color:var(--white);font-size:19px}
.apptab.on{background:var(--green)}
.subnav{left:0;top:98px;width:1200px;height:41px;background:var(--green);color:var(--white);font-size:14px}
.subnav span{position:absolute;top:0;height:41px;display:flex;align-items:center}
.subnav .on{background:var(--green-dark);padding:0 10px}
h1{position:absolute;left:134px;top:162px;font-size:36px;font-weight:700;color:#222}
.ftab{top:169px;height:32px;background:var(--blue);color:var(--white);font-size:16px;font-weight:700;border-radius:4px 4px 0 0}
.ftab.on{background:var(--green)}
.ftab i{display:inline-block;width:10px;height:10px;border-radius:50%;background:var(--green);margin:-10px 0 0 3px}
.panel{left:130px;top:201px;width:940px;height:884px;border:2px solid var(--green)}
.toolbar{left:130px;top:201px;width:940px;height:26px;background:var(--green);color:var(--white);font-size:12px;font-weight:500}
.tb{position:absolute;top:0;height:26px;background:var(--blue);display:flex;align-items:center;justify-content:center;gap:5px;border-right:1px solid #3a72b5}
.tb.g{background:var(--green)}
.lbl{font-size:16px;font-weight:500;color:#333}
.inp{position:absolute;height:30px;border:1px solid var(--field);background:var(--white)}
.btn-g{background:var(--green);color:var(--white);font-size:15px;font-weight:500;display:flex;align-items:center;gap:8px;padding-left:6px}
.stab{top:703px;height:33px;background:var(--blue);color:var(--white);font-size:16px;font-weight:700;border-radius:4px 4px 0 0}
.stab.on{background:var(--green)}
.inner{left:160px;top:736px;width:883px;height:319px;border:2px solid var(--green)}
.rl{position:absolute;font-size:16px;color:#333;text-align:right}
.sel{position:absolute;height:25px;border:1px solid var(--field);background:var(--white)}
.sel svg{position:absolute;right:5px;top:8px}
.footer{left:0;top:1110px;width:1200px;height:60px;background:var(--blue)}
.footer .msg{position:absolute;left:360px;top:0;width:480px;height:60px;background:var(--green);color:var(--white);font-size:18px;font-weight:500;display:flex;align-items:center;justify-content:center;gap:22px}
</style>
</head>
<body>
<div class="abs topbar">
  <div class="cell" style="left:16px">Logged In As</div>
  <div class="cell hl" style="left:130px;width:133px">Owen Marsh
    <svg width="16" height="16" viewBox="0 0 16 16"><circle cx="8" cy="8" r="5" fill="none" stroke="#fff" stroke-width="3" stroke-dasharray="2.5 1.4"/><circle cx="8" cy="8" r="2" fill="#fff"/></svg></div>
  <div class="cell" style="left:274px">Current Role</div>
  <div class="cell hl" style="left:381px;width:155px">Administrator
    <svg width="16" height="16" viewBox="0 0 16 16"><circle cx="8" cy="8" r="7" fill="none" stroke="#fff" stroke-width="1.5"/><path d="M4.5 6.5h7L8 10.5z" fill="#fff"/></svg></div>
  <div class="toplinks abs"><span>Touch</span><span>New Tab</span><span>Help</span><span>Support</span><span>Log out</span></div>
</div>

<div class="abs apptab flex" style="left:10px;width:86px">Home</div>
<div class="abs apptab flex" style="left:97px;width:88px">eSource</div>
<div class="abs apptab flex on" style="left:186px;width:87px">eBuy</div>
<div class="abs apptab flex" style="left:274px;width:95px">eRequest</div>
<div class="abs apptab flex" style="left:370px;width:87px">eSell</div>
<div class="abs apptab flex" style="left:458px;width:87px">eStock</div>
<div class="abs apptab flex" style="left:546px;width:87px">ePlan</div>
<div class="abs apptab flex" style="left:634px;width:109px">Preferences</div>
<div class="abs logo">BRINDLECOVE</div>

<div class="abs subnav">
  <span class="on" style="left:20px;width:62px">Orders</span>
  <span style="left:90px">Receipts</span><span style="left:163px">Shipments</span>
  <span style="left:249px">Invoices</span><span style="left:320px">Pricing</span>
  <span style="left:383px">Tables</span><span style="left:442px">Reports</span>
  <span style="left:510px">Inquiries</span><span style="left:582px">Periodic Tasks</span>
  <span style="left:697px">Workflows</span>
</div>

<h1>Purchase Order</h1>
<div class="abs ftab flex on" style="left:667px;width:100px">Header</div>
<div class="abs ftab flex" style="left:769px;width:98px">Lines<i></i></div>
<div class="abs ftab flex" style="left:869px;width:100px">Charges</div>
<div class="abs ftab flex" style="left:971px;width:99px">Notes<i></i></div>

<div class="abs panel"></div>
<div class="abs toolbar">
  <div class="tb" style="left:0;width:26px"><svg width="10" height="12"><path d="M7 3 3 8a1.5 1.5 0 0 0 2 2l4-5a3 3 0 0 0-4-4L1 6" fill="none" stroke="#fff" stroke-width="1.4"/></svg></div>
  <div class="tb" style="left:26px;width:26px"><svg width="10" height="12"><rect x="1" y="1" width="8" height="10" fill="none" stroke="#fff" stroke-width="1.4"/></svg></div>
  <div class="tb" style="left:52px;width:26px"><svg width="12" height="12"><circle cx="9" cy="2.5" r="2" fill="#fff"/><circle cx="3" cy="6" r="2" fill="#fff"/><circle cx="9" cy="9.5" r="2" fill="#fff"/><path d="M9 2.5 3 6l6 3.5" stroke="#fff" fill="none"/></svg></div>
  <div class="tb" style="left:78px;width:26px"><svg width="12" height="12"><path d="M2 11 7 6M7 2a3 3 0 0 0 3 4" stroke="#fff" stroke-width="2" fill="none"/></svg></div>
  <div class="tb" style="left:104px;width:26px"><svg width="12" height="12"><circle cx="6" cy="6" r="5.5" fill="#fff"/><text x="6" y="9" font-size="8" font-weight="700" text-anchor="middle" fill="#0b51a1">?</text></svg></div>
  <div class="tb" style="left:130px;width:90px"><svg width="12" height="12"><path d="M1 3v8h8V7M5 7l6-6M7 1h4v4" stroke="#fff" stroke-width="1.5" fill="none"/></svg>Post Order</div>
  <div class="tb" style="left:610px;width:66px"><svg width="11" height="11"><circle cx="4.5" cy="4.5" r="3.3" stroke="#9ccf63" stroke-width="1.6" fill="none"/><path d="M7 7l3 3" stroke="#9ccf63" stroke-width="1.8"/></svg>search</div>
  <div class="tb" style="left:676px;width:66px"><svg width="11" height="11"><circle cx="5.5" cy="5.5" r="5.5" fill="#9ccf63"/><path d="M5.5 2.5v6M2.5 5.5h6" stroke="#0b51a1" stroke-width="1.6"/></svg>new</div>
  <div class="tb" style="left:742px;width:66px"><svg width="12" height="10"><path d="M1 5l3.5 3.5L11 1.5" stroke="#9ccf63" stroke-width="2" fill="none"/></svg>apply</div>
  <div class="tb" style="left:808px;width:66px"><svg width="10" height="12"><rect x="1.5" y="3" width="7" height="9" fill="#e0322e"/><rect x="0" y="1" width="10" height="2" fill="#e0322e"/></svg>delete</div>
  <div class="tb" style="left:874px;width:66px;border-right:none"><svg width="12" height="12"><path d="M3 4a4 4 0 1 1 0 4" stroke="#9ccf63" stroke-width="1.6" fill="none"/><path d="M1 1v4h4" fill="#9ccf63"/></svg>back</div>
</div>

<div class="abs lbl" style="left:141px;top:241px">Order #</div>
<div class="abs" style="left:141px;top:263px;font-size:16px">100159</div>
<div class="abs btn-g" style="left:227px;top:248px;width:190px;height:25px;font-size:14px">
  <svg width="18" height="18"><circle cx="9" cy="9" r="9" fill="#fff"/><rect x="8" y="8" width="2" height="6" fill="#9ccf63"/><circle cx="9" cy="5.5" r="1.2" fill="#9ccf63"/></svg>Regular Purchase Order</div>

<div class="abs lbl" style="left:140px;top:295px">Ship From</div>
<div class="inp" style="left:140px;top:315px;width:120px;height:20px"></div>
<div class="abs" style="left:269px;top:311px;font-size:22px">/</div>
<div class="inp" style="left:288px;top:315px;width:26px;height:20px"></div>
<div class="inp" style="left:140px;top:350px;width:500px"></div>
<div class="abs lbl" style="left:140px;top:389px">Address</div>
<div class="inp" style="left:140px;top:409px;width:500px"></div>
<div class="inp" style="left:140px;top:449px;width:500px"></div>
<div class="abs" style="left:649px;top:457px;font-size:14px;color:var(--green)">DPV Unconfirmed</div>
<div class="abs lbl" style="left:140px;top:498px">City</div>
<div class="inp" style="left:140px;top:518px;width:375px"></div>
<div class="abs lbl" style="left:545px;top:495px">State</div>
<div class="inp" style="left:545px;top:518px;width:96px"></div>
<div class="abs" style="left:652px;top:521px;display:flex;align-items:center;gap:6px;font-size:16px">
  <svg width="14" height="14"><rect width="14" height="14" fill="#9ccf63"/><path d="M3 7l3 3 5-6" stroke="#fff" stroke-width="2" fill="none"/></svg>Accept</div>
<div class="abs lbl" style="left:139px;top:555px">Country</div>
<div class="inp" style="left:140px;top:578px;width:374px"></div>
<div class="abs lbl" style="left:549px;top:557px">Zip</div>
<div class="inp" style="left:545px;top:580px;width:96px"></div>
<div class="abs btn-g" style="left:140px;top:618px;width:134px;height:25px;font-size:16px">
  <svg width="16" height="16"><rect x="1" y="0" width="14" height="16" rx="2" fill="#fff"/><circle cx="8" cy="6" r="2.5" fill="#9ccf63"/><path d="M3.5 13a4.5 4 0 0 1 9 0z" fill="#9ccf63"/></svg>Add Contact</div>

<div class="abs stab flex" style="left:160px;width:100px">Order Info</div>
<div class="abs stab flex on" style="left:262px;width:98px">Shipping</div>
<div class="abs stab flex" style="left:362px;width:99px">Payment</div>
<div class="abs stab flex" style="left:463px;width:99px">Accounts</div>
<div class="abs stab flex" style="left:564px;width:129px">Totals/Approval</div>
<div class="abs inner"></div>

<div class="rl" style="right:909px;top:753px">Receive At</div>
<div class="rl" style="right:909px;top:788px">Carrier</div>
<div class="rl" style="right:909px;top:823px">Express Service</div>
<div class="rl" style="right:909px;top:858px">FOB</div>
<div class="rl" style="right:909px;top:893px">Order Ship Rule</div>
<div class="rl" style="right:909px;top:928px">Line Ship Rule</div>
<div class="sel" style="left:306px;top:749px;width:180px"><svg width="10" height="7"><path d="M1 1l4 4 4-4" stroke="#9ccf63" stroke-width="1.8" fill="none"/></svg></div>
<div class="sel" style="left:306px;top:784px;width:180px"><svg width="10" height="7"><path d="M1 1l4 4 4-4" stroke="#9ccf63" stroke-width="1.8" fill="none"/></svg></div>
<div class="sel" style="left:306px;top:819px;width:180px"><svg width="10" height="7"><path d="M1 1l4 4 4-4" stroke="#9ccf63" stroke-width="1.8" fill="none"/></svg></div>
<div class="sel" style="left:306px;top:854px;width:180px"><svg width="10" height="7"><path d="M1 1l4 4 4-4" stroke="#9ccf63" stroke-width="1.8" fill="none"/></svg></div>
<div class="sel" style="left:306px;top:889px;width:180px"><svg width="10" height="7"><path d="M1 1l4 4 4-4" stroke="#9ccf63" stroke-width="1.8" fill="none"/></svg></div>
<div class="sel" style="left:306px;top:924px;width:180px"><svg width="10" height="7"><path d="M1 1l4 4 4-4" stroke="#9ccf63" stroke-width="1.8" fill="none"/></svg></div>

<div class="rl" style="right:576px;top:753px">Request Date</div>
<div class="rl" style="right:576px;top:788px">Freight Terms</div>
<div class="rl" style="right:576px;top:823px">Freight Calc</div>
<div class="rl" style="right:576px;top:893px">Customer Ship To</div>
<div class="sel" style="left:639px;top:749px;width:180px"><svg width="14" height="14" style="top:5px"><rect x="1" y="2" width="12" height="11" fill="#9ccf63"/><path d="M1 5h12M5 5v8M9 5v8M1 9h12" stroke="#fff"/></svg></div>
<div class="sel" style="left:641px;top:784px;width:180px"><svg width="10" height="7"><path d="M1 1l4 4 4-4" stroke="#9ccf63" stroke-width="1.8" fill="none"/></svg></div>
<div class="sel" style="left:641px;top:819px;width:180px"><svg width="10" height="7"><path d="M1 1l4 4 4-4" stroke="#9ccf63" stroke-width="1.8" fill="none"/></svg></div>
<div class="sel" style="left:641px;top:889px;width:111px"></div>
<div class="abs" style="left:762px;top:887px;font-size:22px">/</div>
<div class="sel" style="left:781px;top:889px;width:40px"></div>

<div class="abs footer">
  <div class="msg">
    <svg width="32" height="32" viewBox="0 0 32 32"><path d="M3 2h26a2 2 0 0 1 2 2v18a2 2 0 0 1-2 2H14l-6 7v-7H3a2 2 0 0 1-2-2V4a2 2 0 0 1 2-2z" fill="#fff"/></svg>
    Enter property values, and click Apply
  </div>
</div>
</body>
</html>
```